New Business Card Design Project

Use the flyer uploaded and website www.brightoakbuilders.com for inspiration.
List Our Services on Backside of business cards
Martin Hollis
Harborline Renovations Inc.
Licensed General Contractors
858-471-9063

Contact Information for Business Card

Use the flyer uploaded and website www.brightoakbuilders.com for inspiration. List Our Services on Backside of business cards Martin Hollis Harborline Renovations Inc. Licensed General Contractors 858-471-9063

```html
<!DOCTYPE html>
<html lang="en">
<head>
<meta charset="utf-8">
<title>Harborline Renovations – Business Card</title>
<link href="https://fonts.googleapis.com/css2?family=Open+Sans:wght@400;700&display=swap" rel="stylesheet">
<style>
  :root {
    --page-bg: #232323;
    --card-bg: #111111;
    --ink: #f4f4f4;
    --ink-soft: #d8d8d8;
    --rule: #e8e8e8;
  }
  * { margin: 0; padding: 0; box-sizing: border-box; }
  html, body {
    width: 1200px; height: 780px; overflow: hidden;
    background: var(--page-bg);
    font-family: "Open Sans", Arial, sans-serif;
    color: var(--ink);
  }
  .sheet {
    width: 1200px; height: 780px;
    display: flex; align-items: center; justify-content: center; gap: 40px;
  }
  .card {
    width: 540px; height: 309px;
    background: var(--card-bg);
    border-radius: 22px;
    position: relative;
    box-shadow: 0 10px 28px rgba(0,0,0,.45);
  }
  .brand-name {
    font-weight: 400;
    text-transform: uppercase;
    text-align: center;
    color: var(--ink);
    letter-spacing: .14em;
  }
  .icon { width: 14px; height: 14px; flex: none; fill: none; stroke: var(--ink); stroke-width: 1.6; stroke-linecap: round; stroke-linejoin: round; }

  /* Back: services */
  .card--back { padding: 34px 30px 26px; }
  .card--back .brand-name { font-size: 20px; margin-bottom: 26px; }
  .services-title {
    font-size: 12.5px; text-align: center; letter-spacing: .02em; margin-bottom: 22px;
  }
  .service-columns { display: flex; justify-content: space-between; }
  .service-list { list-style: none; font-size: 13px; line-height: 1.75; }
  .service-list li { display: flex; align-items: center; gap: 7px; }
  .service-list--right li { justify-content: flex-end; }

  /* Front: identity */
  .card--front .brand-name {
    position: absolute; top: 82px; left: 0; right: 0;
    font-size: 30px; letter-spacing: .12em;
  }
  .brand-mark {
    position: absolute; top: 40px; left: 50%; transform: translateX(-50%);
    width: 20px; height: 20px; border: 1.5px solid var(--ink); border-radius: 50%;
  }
  .contact-row {
    position: absolute; left: 40px; right: 40px; bottom: 42px;
    display: flex; align-items: center; gap: 22px;
  }
  .person-name { font-size: 22px; font-weight: 700; line-height: 1.2; }
  .person-company { font-size: 13px; color: var(--ink-soft); }
  .divider { width: 1px; height: 54px; background: var(--rule); }
  .contact-list { list-style: none; font-size: 14px; line-height: 1.8; }
  .contact-list li { display: flex; align-items: center; gap: 8px; }
</style>
</head>
<body>
<svg width="0" height="0" style="position:absolute" aria-hidden="true">
  <defs>
    <symbol id="tick" viewBox="0 0 16 16"><circle cx="8" cy="8" r="6.6"/><path d="M5 8.2l2.2 2.3L12.5 3.5"/></symbol>
    <symbol id="phone" viewBox="0 0 16 16"><path d="M4 2l2.2 2.6-1.3 1.6c.8 1.9 2.3 3.4 4.2 4.2l1.6-1.3L13.3 11.3 12 13.6C7 13.3 2.7 9 2.4 4z"/></symbol>
    <symbol id="globe" viewBox="0 0 16 16"><circle cx="8" cy="8" r="6.2"/><path d="M1.8 8h12.4M8 1.8c2.2 2 2.2 10.4 0 12.4M8 1.8c-2.2 2-2.2 10.4 0 12.4"/></symbol>
  </defs>
</svg>

<main class="sheet">
  <section class="card card--back" aria-label="Card back: services">
    <p class="brand-name">Harborline Renovations</p>
    <p class="services-title">OUR SERVICES ARE 100% GUARANTEED SPECIALIZING IN:</p>
    <div class="service-columns">
      <ul class="service-list service-list--left">
        <li><svg class="icon"><use href="#tick"/></svg>Remodel: Kitchen &amp; Bath</li>
        <li><svg class="icon"><use href="#tick"/></svg>Painting: Interior &amp; Exterior</li>
        <li><svg class="icon"><use href="#tick"/></svg>Flooring: Carpect, Vinyl, Wood</li>
        <li><svg class="icon"><use href="#tick"/></svg>Window &amp; Door Replacement</li>
      </ul>
      <ul class="service-list service-list--right">
        <li>Plumbing: Repairs &amp; Upgrades<svg class="icon"><use href="#tick"/></svg></li>
        <li>Energy-Efficient Upgrades<svg class="icon"><use href="#tick"/></svg></li>
        <li>Deck &amp; Patio Construction<svg class="icon"><use href="#tick"/></svg></li>
        <li>Water &amp; Mold Damage<svg class="icon"><use href="#tick"/></svg></li>
        <li>Garage Renovation<svg class="icon"><use href="#tick"/></svg></li>
      </ul>
    </div>
  </section>

  <section class="card card--front" aria-label="Card front: contact">
    <span class="brand-mark" aria-hidden="true"></span>
    <p class="brand-name">Harborline Renovations</p>
    <div class="contact-row">
      <div class="person">
        <p class="person-name">Martin Hollis</p>
        <p class="person-company">Harborline Renovations Inc.</p>
      </div>
      <span class="divider" aria-hidden="true"></span>
      <ul class="contact-list">
        <li><svg class="icon"><use href="#phone"/></svg>858-471-9063</li>
        <li><svg class="icon"><use href="#globe"/></svg>www.brightoakbuilders.com</li>
      </ul>
    </div>
  </section>
</main>
</body>
</html>
```